Gate Bolts Express

THIS IS A DESIGN & BUILD COMPETITION

Im Looking for a fresh E-commerce website to sell door locks, I would like it to be more visually based, so instead of having worded categories, have then visual, with rim cylinders, euro cylinders, garage locks, oval cylinders, deadlocks, sash locks, Upvc multipoint locks, door handles, window handles, safes, padlocks etc, as picture, with a product manufacturer search feature, a video tab or banner to stream videos,
Updates

Hi Everyone,

Im looking for a fully functioning e-commerce website not a logo

Thanks
Neil

I really like this website http://steadyporch.com.au/ so make it similar to this with the blues from my logo, I will upload some random stock pictures later

Hi Everyone,

Im overwhelmed by some of the designs which have been great, however I think I need to make my vision clearer, Im looking for 12 - 16 categories - euro cylinders, rim cylinders, sashlocks, deadlocks, door handles, garage locks, safes, multipoint locks, panic hardware, padlocks, nightlatches, Post Boxes.

these are only categories, once the customer clicks on the category they will have a choice of manufacturers which will be between 4/5 Brisk, Halvern, Orbo, Fen-d-bar, Pikt, Marchwood.

The reason for this is people generally dont know what the lock on their door is called and I want a site to be visual to enable customers to source the locks they need.

This is what will make my site unique!!!!

Colour is important, I want to use the blue from my logo to keep it uniformed

I like the idea of reviewed products down the left hand side

I would like a product/ manufacturer search facility 

All the above are in your designs, but they are not all on 1 design ;0)

Thanks Everyone
Neil

Hi everyone,

Done some paint shop lol with one of the submitted designs just to show yous guys what im looking for

The12 pictures in the main part of the page are categories, not sale items

Thanks

Neil

Reason: I have extended the design period as there has been a misunderstanding with this competition, The competition is for design and build

Hi Everyone,

I have extended this competition as there was a misunderstanding with this project, It is for full design and build of an ecommerce website, not just design, I will put the prize money upto £1000 total fund, so please if you cant build your design then please withdraw them.

Thanks
Neil

Target Market(s)

The market is for DIY customers wanting to change their own locks.

Industry/Entity Type

Garage

Requirements
Must have
• It must be visually based, to help customers identify the product they need,

It must also have a banner/ picture of how to measure a euro cylinder.

I think it would work best if we have a generic category picture, then when you click the picture it then has a manufacturer page in pictures again with a brief description of what the lock offers ie, anti bump, anti snap, anti drill, British Standard etc.

must be easy to populate with stock
Nice to have
• I would like it to have geolocation for visitors ip addresses so I can see where they are staying so I can offer a fitting service.

```html
<!DOCTYPE html>
<html lang="en">
<head>
<meta charset="utf-8">
<title>Gate Bolts Express</title>
<link href="https://fonts.googleapis.com/css2?family=Open+Sans:wght@400;600;700&family=Oswald:wght@500;700&display=swap" rel="stylesheet">
<style>
:root{
  --blue:#1b5fbf;
  --blue-dark:#0f4290;
  --navy:#0b2a57;
  --navy-2:#08203f;
  --page:#e4e8ee;
  --panel:#ffffff;
  --line:#d6dbe2;
  --soft:#f2f4f7;
  --text:#555b63;
  --muted:#8b929b;
  --green:#3aa635;
  --red:#c62828;
}
*{box-sizing:border-box;margin:0;padding:0}
html,body{width:896px;height:1200px;overflow:hidden}
body{background:var(--page);font-family:"Open Sans",Arial,sans-serif;color:var(--text);position:relative}
.abs{position:absolute}

/* header */
.site-header{left:0;top:0;width:896px;height:90px;background:#fff}
.brand{left:84px;top:30px}
.brand-name{font-family:"Open Sans",Arial,sans-serif;font-weight:700;font-size:22px;line-height:28px;color:var(--blue);white-space:nowrap}
.account-links{left:540px;top:0;height:24px;width:274px;border:1px solid var(--line);border-top:none;display:flex;font-size:8px;color:var(--muted)}
.account-links span{flex:1;display:flex;align-items:center;justify-content:center;gap:3px;border-left:1px solid var(--line)}
.account-links span:first-child{border-left:none}
.account-links i{width:6px;height:6px;background:var(--blue);display:inline-block}
.site-search{left:540px;top:44px;width:160px;height:18px;border:1px solid var(--line);font-size:8px;color:var(--muted);padding:3px 6px;display:flex;justify-content:space-between}
.lang-select{left:708px;top:44px;width:106px;height:18px;border:1px solid var(--line);font-size:8px;color:var(--muted);padding:3px 6px;display:flex;justify-content:space-between}

/* nav */
.main-nav{left:0;top:90px;width:896px;height:30px;background:var(--blue)}
.main-nav ul{position:absolute;left:84px;top:0;height:30px;display:flex;list-style:none}
.main-nav li{color:#fff;font-size:9.5px;font-weight:600;padding:0 11px;line-height:30px;border-right:1px solid rgba(255,255,255,.2)}
.main-nav li.active{background:var(--blue-dark)}
.nav-phone{left:664px;top:0;height:30px;display:flex;align-items:center;gap:6px;color:#fff;font-weight:700;font-size:14px}

/* panels */
.panel{background:var(--panel);border:1px solid var(--line)}
.panel-title{font-family:"Oswald",sans-serif;font-weight:500;font-size:12px;color:var(--navy);padding:8px 10px 6px;text-transform:uppercase;letter-spacing:.3px}

/* search product */
.product-search{left:84px;top:136px;width:212px;height:306px}
.field{margin:0 10px 9px}
.field label{display:block;font-size:8px;color:var(--muted);margin-bottom:3px}
.field .select{height:19px;border:1px solid var(--line);font-size:8px;padding:3px 6px;display:flex;justify-content:space-between;color:var(--text)}
.btn-blue{background:var(--blue);color:#fff;font-size:8px;font-weight:700;text-transform:uppercase;padding:5px 9px;display:inline-block}
.product-search .btn-blue{position:absolute;right:10px;bottom:14px}

/* video */
.video-box{left:84px;top:456px;width:212px;height:160px;padding:6px}
.video-screen{width:100%;height:118px;background:linear-gradient(135deg,#6d5a4a,#c9b8a4 55%,#3d3a38);position:relative}
.video-play{position:absolute;left:50%;top:50%;transform:translate(-50%,-50%)}
.video-bar{height:22px;margin-top:6px;background:var(--soft);display:flex;align-items:center;gap:6px;padding:0 6px}
.video-bar span{flex:1;height:3px;background:var(--line)}

/* reviews */
.reviews{left:84px;top:630px;width:212px;height:262px}
.review{display:flex;gap:8px;margin:4px 10px 10px}
.review-thumb{width:46px;height:46px;flex:none;border:1px solid var(--line);background:linear-gradient(135deg,#e9e2cf,#c7a94f)}
.review p{font-size:7.5px;line-height:11px}
.review b{display:block;color:var(--blue);font-size:8px}
.reviews .btn-blue{position:absolute;right:10px;bottom:10px}

/* best sellers */
.best-sellers{left:84px;top:906px;width:212px;height:160px}
.best-item{display:flex;gap:10px;margin:4px 10px}
.best-thumb{width:70px;height:78px;flex:none;background:linear-gradient(160deg,#f1f1f1,#8f969e)}
.best-name{font-size:8px;font-weight:600;margin-top:6px}
.price{margin-top:8px;font-size:13px;font-weight:700;color:var(--red)}
.price s{font-size:10px;color:var(--muted);font-weight:400;margin-left:4px}
.btn-green{margin-top:10px;background:var(--green);color:#fff;font-size:8px;font-weight:700;padding:5px 8px;display:inline-block;text-transform:uppercase}

/* slider */
.hero-slider{left:312px;top:136px;width:502px;height:270px;padding:6px}
.hero-image{width:100%;height:100%;background:linear-gradient(120deg,#3c4148,#9aa2ab 45%,#d6d9dd 60%,#5f666e);position:relative}
.hero-caption{position:absolute;left:14px;top:150px;width:190px;background:rgba(0,0,0,.6);color:#fff;padding:8px 10px}
.hero-caption h2{font-family:"Oswald",sans-serif;font-size:13px;font-weight:500;text-transform:uppercase}
.hero-caption p{font-size:7.5px;line-height:11px;margin-top:3px}
.hero-arrow{position:absolute;top:112px;width:16px;height:30px;background:rgba(255,255,255,.85);display:flex;align-items:center;justify-content:center}
.hero-arrow.prev{left:0}.hero-arrow.next{right:0}

/* categories */
.categories{left:312px;top:418px;width:502px;height:648px}
.categories-head{height:28px;background:var(--soft);border-bottom:1px solid var(--line);font-family:"Oswald",sans-serif;font-size:13px;font-weight:500;color:var(--blue);padding:5px 12px}
.category-grid{display:grid;grid-template-columns:repeat(3,1fr);grid-template-rows:repeat(4,1fr);height:618px;gap:0}
.category{border-right:1px solid var(--line);border-bottom:1px solid var(--line);padding:8px 10px}
.category:nth-child(3n){border-right:none}
.category:nth-last-child(-n+3){border-bottom:none}
.category h3{font-family:"Oswald",sans-serif;font-weight:500;font-size:10.5px;color:var(--blue);text-transform:uppercase}
.category-img{height:80px;margin:8px 22px;background:radial-gradient(circle at 50% 50%,#d9c892 0,#eee9dc 40%,#fafafa 70%)}
.category-img.steel{background:radial-gradient(circle at 50% 50%,#a9b0b8 0,#e3e6ea 40%,#fafafa 70%)}
.category p{font-size:7.5px;line-height:10px;color:var(--muted)}

/* footer */
.site-footer{left:0;top:1082px;width:896px;height:118px;background:var(--navy)}
.foot-col{position:absolute;top:14px;color:#fff}
.foot-col h4{font-size:10px;font-weight:700;margin-bottom:8px}
.cards{display:grid;grid-template-columns:repeat(4,30px);gap:5px}
.cards span{height:18px;background:#dfe6f0;border-radius:2px}
.news-input{width:120px;height:16px;background:#fff;font-size:7.5px;color:var(--muted);padding:2px 6px;margin-bottom:5px}
.news-row{display:flex;gap:5px;align-items:flex-start}
.btn-submit{background:var(--navy-2);color:#fff;font-size:8px;font-weight:700;padding:3px 10px;border:1px solid #2a4a7a}
.socials{display:flex;gap:6px;margin-bottom:10px}
.socials span{width:16px;height:16px;background:#2f5d9a}
.foot-links{font-size:8px;color:#c9d5e6}
.copyright{font-size:7.5px;color:#8ea3c0;margin-top:6px}
</style>
</head>
<body>

<header class="site-header abs">
  <div class="brand abs"><span class="brand-name">Gate Bolts Express</span></div>
  <div class="account-links abs">
    <span><i></i>Shopping Cart</span><span><i></i>My Account</span><span><i></i>Checkout</span><span><i></i>Log in</span>
  </div>
  <div class="site-search abs"><span>Search</span>
    <svg width="9" height="9" viewBox="0 0 10 10"><circle cx="4" cy="4" r="3" fill="none" stroke="#8b929b" stroke-width="1.3"/><path d="M6.3 6.3 9 9" stroke="#8b929b" stroke-width="1.3"/></svg></div>
  <div class="lang-select abs"><span>English</span><span>▾</span></div>
</header>

<nav class="main-nav abs">
  <ul>
    <li class="active">Home</li><li>About Us</li><li>New Arrivals</li><li>Best Sellers</li><li>Clearance</li><li>FAQ</li><li>Testimonials</li><li>Contact Us</li>
  </ul>
  <div class="nav-phone abs">
    <svg width="14" height="14" viewBox="0 0 24 24"><path fill="#fff" d="M6.6 10.8a15 15 0 0 0 6.6 6.6l2.2-2.2c.3-.3.7-.4 1-.2 1.1.4 2.3.6 3.6.6.6 0 1 .4 1 1V20c0 .6-.4 1-1 1A17 17 0 0 1 3 4c0-.6.4-1 1-1h3.5c.6 0 1 .4 1 1 0 1.3.2 2.5.6 3.6.1.3 0 .7-.2 1z"/></svg>
    210-555-0148
  </div>
</nav>

<section class="product-search panel abs">
  <h2 class="panel-title">Search Product</h2>
  <div class="field"><label>Location</label><div class="select"><span>Doors</span><span>▾</span></div></div>
  <div class="field"><label>Manufacturer</label><div class="select"><span>Choose Brand</span><span>▾</span></div></div>
  <div class="field"><label>Cylinder Type</label><div class="select"><span>Any</span><span>▾</span></div></div>
  <div class="field"><label>Price Range</label><div class="select"><span>$0 - $100</span><span>▾</span></div></div>
  <span class="btn-blue">Search Now</span>
</section>

<section class="video-box panel abs">
  <div class="video-screen" role="img" aria-label="Video still of a locksmith fitting a cylinder">
    <svg class="video-play" width="30" height="30" viewBox="0 0 30 30"><circle cx="15" cy="15" r="14" fill="rgba(0,0,0,.55)"/><path d="M12 9v12l9-6z" fill="#fff"/></svg>
  </div>
  <div class="video-bar">
    <svg width="8" height="8" viewBox="0 0 8 8"><path d="M1 0v8l7-4z" fill="#555b63"/></svg><span></span>
  </div>
</section>

<section class="reviews panel abs">
  <h2 class="panel-title">Recent Review Items</h2>
  <div class="review"><div class="review-thumb" role="img" aria-label="Euro cylinder product photo"></div><p><b>Euro Cylinder</b>Euro cylinder fitted easily, quick delivery, great value.</p></div>
  <div class="review"><div class="review-thumb" role="img" aria-label="Padlock product photo"></div><p><b>Padlock</b>Strong padlock, feels solid, would buy again here.</p></div>
  <div class="review"><div class="review-thumb" role="img" aria-label="Door handle product photo"></div><p><b>Door Handle</b>Door handle matched perfectly, clear photos helped me.</p></div>
  <span class="btn-blue">More</span>
</section>

<section class="best-sellers panel abs">
  <h2 class="panel-title">Best Sellers</h2>
  <div class="best-item">
    <div class="best-thumb" role="img" aria-label="Best selling lock product photo"></div>
    <div>
      <div class="best-name">Brass Padlock 50mm</div>
      <div class="price">$99.00<s>$109.00</s></div>
      <span class="btn-green">Add to Cart</span>
    </div>
  </div>
</section>

<section class="hero-slider panel abs">
  <div class="hero-image" role="img" aria-label="Close-up photo of a garage door lock">
    <div class="hero-arrow prev"><svg width="7" height="10" viewBox="0 0 7 10"><path d="M6 1 2 5l4 4" fill="none" stroke="#555" stroke-width="1.6"/></svg></div>
    <div class="hero-arrow next"><svg width="7" height="10" viewBox="0 0 7 10"><path d="M1 1l4 4-4 4" fill="none" stroke="#555" stroke-width="1.6"/></svg></div>
    <div class="hero-caption"><h2>Garage Locks</h2><p>Heavy duty garage locks to keep your tools and car secure all year.</p></div>
  </div>
</section>

<section class="categories panel abs">
  <h2 class="categories-head">Featured Categories</h2>
  <div class="category-grid">
    <article class="category"><h3>Rim Cylinders</h3><div class="category-img" role="img" aria-label="Rim cylinder photo"></div><p>Rim cylinders for nightlatches, supplied with three keys as standard.</p></article>
    <article class="category"><h3>Euro Cylinders</h3><div class="category-img steel" role="img" aria-label="Euro cylinder photo"></div><p>Anti snap euro cylinders in many sizes for uPVC doors.</p></article>
    <article class="category"><h3>Garage Locks</h3><div class="category-img steel" role="img" aria-label="Garage lock photo"></div><p>Strong garage locks for up and over doors and sheds.</p></article>
    <article class="category"><h3>Oval Cylinders</h3><div class="category-img steel" role="img" aria-label="Oval cylinder photo"></div><p>Oval cylinders to fit older mortice locks and door sets.</p></article>
    <article class="category"><h3>Deadlocks</h3><div class="category-img" role="img" aria-label="Deadlock photo"></div><p>British Standard deadlocks with five levers for insurance approved security.</p></article>
    <article class="category"><h3>Sash Locks</h3><div class="category-img" role="img" aria-label="Sash lock photo"></div><p>Sash locks combining a latch and deadbolt for wooden doors.</p></article>
    <article class="category"><h3>uPVC Multipoint Locks</h3><div class="category-img steel" role="img" aria-label="Multipoint lock strip photo"></div><p>Replacement uPVC multipoint gearboxes plus full length lock strips available.</p></article>
    <article class="category"><h3>Door Handles</h3><div class="category-img" role="img" aria-label="Door handle photo"></div><p>Lever and pull door handles in chrome, brass and satin.</p></article>
    <article class="category"><h3>Window Handles</h3><div class="category-img" role="img" aria-label="Window handle photo"></div><p>Locking window handles with keys for uPVC and aluminium frames.</p></article>
    <article class="category"><h3>Safes</h3><div class="category-img steel" role="img" aria-label="Home safe photo"></div><p>Fire resistant home safes with key or digital code locks.</p></article>
    <article class="category"><h3>Padlocks</h3><div class="category-img" role="img" aria-label="Padlock photo"></div><p>Weatherproof padlocks with hardened shackles for gates, sheds and bikes.</p></article>
    <article class="category"><h3>Oval Cylinders</h3><div class="category-img steel" role="img" aria-label="Oval cylinder photo"></div><p>High security oval cylinders with anti drill pins and keys.</p></article>
  </div>
</section>

<footer class="site-footer abs">
  <div class="foot-col" style="left:84px">
    <h4>Payments</h4>
    <div class="cards"><span></span><span></span><span></span><span></span><span></span><span></span><span></span><span></span></div>
  </div>
  <div class="foot-col" style="left:380px">
    <h4>Newsletter</h4>
    <div class="news-input">Enter Name</div>
    <div class="news-row"><div class="news-input">Enter Email</div><span class="btn-submit">SUBMIT</span></div>
  </div>
  <div class="foot-col" style="left:640px">
    <div class="socials"><span></span><span></span><span></span><span></span><span></span></div>
    <div class="foot-links">Help | Terms | Privacy Policy | Sitemap</div>
    <div class="copyright">Copyright 2013 gateboltsexpress.co.uk All rights reserved</div>
  </div>
</footer>

</body>
</html>
```